ATM BUSINESS MACHINES...

NEED A NEW LOGO AND BUSINESS CARD FOR A BRAND NEW ATM BUSINESS. WE GO TO LOCAL BUSINESSES AND PLACE ATM'S IN THER STORES FOR FREE. IT INCREASES THEIR BUSINESS. A VERY EYE CATCHY LOGO AND COLOR SCHEME...MODERN, PROFESSIONAL, YET MODERN AND APPEALING....

Target Market(s)

alll types of business owners...young & old....

Industry/Entity Type

Business

Contact Information for Business Card

BRIMWELL QUICK FUNDS-ATM'S
" GET YOUR CASH NOW"
Ray T. Huxley
President/Owner
P.O. Box 87
Harlow Bend, W.K. 29318
bqf.atm@norvexmail.com
Free Atm's- Free Instalation, Free Maintenance Never a cost to business owner......Call now to get you free ATM and increase your sales......

Requirements
Nice to have
• $$$ signs.....colors....raised letters....
Maybe a logo BQF $$$ with ATM machine...

```html
<!DOCTYPE html>
<html lang="en">
<head>
<meta charset="utf-8">
<title>Brimwell Quick Funds – Business Card Colourways</title>
<link rel="stylesheet" href="https://fonts.googleapis.com/css2?family=Bebas+Neue&family=Oswald:wght@500&family=PT+Sans:wght@400&family=Share+Tech+Mono&display=swap">
<style>
  :root {
    --canvas-bg: #e6e6e6;
    --headline-yellow: #ffeb00;
    --band-white: #ffffff;
    --band-ink: #111111;
    --text-white: #ffffff;
    --green: #4e8c3e;
    --green-note: #b7c94a;
    --red: #a01c24;
    --red-note: #e4782c;
    --blue: #4472b6;
    --blue-note: #8db6ea;
  }
  * { box-sizing: border-box; margin: 0; padding: 0; }
  html, body {
    width: 800px; height: 1200px; overflow: hidden;
    background: var(--canvas-bg);
  }
  .sheet { position: relative; width: 800px; height: 1200px; }

  .card {
    position: absolute; left: 200px;
    width: 400px; height: 236px;
    border-radius: 16px;
    background: var(--card-colour);
    box-shadow: 3px 6px 8px rgba(0,0,0,0.45);
    overflow: hidden;
  }
  .card--green { top: 180px; --card-colour: var(--green); --note-colour: var(--green-note); }
  .card--red   { top: 485px; --card-colour: var(--red);   --note-colour: var(--red-note); }
  .card--blue  { top: 790px; --card-colour: var(--blue);  --note-colour: var(--blue-note); }

  .offer-free {
    position: absolute; left: 27px; top: 14px;
    font-family: "Bebas Neue", sans-serif;
    font-size: 62px; line-height: 1;
    color: var(--headline-yellow);
  }
  .offer-list {
    position: absolute; left: 122px; top: 16px;
    list-style: none;
    font-family: "Oswald", sans-serif; font-weight: 500;
    font-size: 10.5px; line-height: 17px;
    color: var(--headline-yellow);
  }
  .offer-note {
    position: absolute; left: 28px;
    font-family: "Oswald", sans-serif; font-weight: 500;
    font-size: 8.5px; line-height: 1;
    color: var(--note-colour);
  }
  .offer-note--first { top: 70px; }
  .offer-note--second { top: 85px; }

  .brand-name {
    position: absolute; right: 18px; top: 18px;
    font-family: "Bebas Neue", sans-serif;
    font-size: 60px; line-height: 1;
    color: var(--text-white);
  }

  .tagline-band {
    position: absolute; left: 0; top: 111px;
    width: 100%; height: 18px;
    background: var(--band-white);
    font-family: "Share Tech Mono", monospace;
    font-size: 11px; line-height: 18px;
    letter-spacing: 1.1px;
    color: var(--band-ink);
    padding-left: 30px;
    white-space: nowrap;
  }

  .contact-line {
    position: absolute; left: 36px; top: 138px;
    font-family: "PT Sans", sans-serif;
    font-size: 12.5px;
    color: var(--text-white);
    white-space: nowrap;
  }
  .person-name {
    position: absolute; left: 34px; top: 173px;
    font-family: "PT Sans", sans-serif;
    font-weight: 400;
    font-size: 20px; line-height: 1;
    color: var(--text-white);
  }
  .person-role {
    position: absolute; left: 35px; top: 197px;
    font-family: "PT Sans", sans-serif;
    font-size: 12.5px; line-height: 1;
    color: var(--text-white);
  }
</style>
</head>
<body>
<main class="sheet">

  <article class="card card--green">
    <div class="offer-free">FREE</div>
    <ul class="offer-list"><li>ATM'S</li><li>INSTALATION</li><li>MAINTENANCE</li></ul>
    <p class="offer-note offer-note--first">NEVER A COST TO BUSINESS OWNER...</p>
    <p class="offer-note offer-note--second">CALL NOW TO GET YOU FREE ATM AND INCREASE YOUR SALES...</p>
    <div class="brand-name">BQF</div>
    <div class="tagline-band">BRIMWELL QUICK FUNDS-ATM'S " GET YOUR CASH NOW"</div>
    <p class="contact-line">P.O. Box 87 Harlow Bend, W.K. 29318 bqf.atm@norvexmail.com</p>
    <h2 class="person-name">RAY T. HUXLEY</h2>
    <p class="person-role">President/Owner</p>
  </article>

  <article class="card card--red">
    <div class="offer-free">FREE</div>
    <ul class="offer-list"><li>ATM'S</li><li>INSTALATION</li><li>MAINTENANCE</li></ul>
    <p class="offer-note offer-note--first">NEVER A COST TO BUSINESS OWNER...</p>
    <p class="offer-note offer-note--second">CALL NOW TO GET YOU FREE ATM AND INCREASE YOUR SALES...</p>
    <div class="brand-name">BQF</div>
    <div class="tagline-band">BRIMWELL QUICK FUNDS-ATM'S " GET YOUR CASH NOW"</div>
    <p class="contact-line">P.O. Box 87 Harlow Bend, W.K. 29318 bqf.atm@norvexmail.com</p>
    <h2 class="person-name">RAY T. HUXLEY</h2>
    <p class="person-role">President/Owner</p>
  </article>

  <article class="card card--blue">
    <div class="offer-free">FREE</div>
    <ul class="offer-list"><li>ATM'S</li><li>INSTALATION</li><li>MAINTENANCE</li></ul>
    <p class="offer-note offer-note--first">NEVER A COST TO BUSINESS OWNER...</p>
    <p class="offer-note offer-note--second">CALL NOW TO GET YOU FREE ATM AND INCREASE YOUR SALES...</p>
    <div class="brand-name">BQF</div>
    <div class="tagline-band">BRIMWELL QUICK FUNDS-ATM'S " GET YOUR CASH NOW"</div>
    <p class="contact-line">P.O. Box 87 Harlow Bend, W.K. 29318 bqf.atm@norvexmail.com</p>
    <h2 class="person-name">RAY T. HUXLEY</h2>
    <p class="person-role">President/Owner</p>
  </article>

</main>
</body>
</html>
```